Brindle Children's Center - Child Care brochure

I just bought a new child care and completely renovated the space. We are also designing a new website, so I need the brochure to match that with updated info. www.brindlechildrenscenter.com - Information on there is current. We expect to have the new one up and running in the next few days. We have new photo's that I'd like to be added to the flyer too. ps. the boys in the pictures are mine, so i would appreciate one of them being added :). support@pixelhavenweb.com has details on the website (dev.brindlechildrenscenter.com). The child care program is only open during the ski season - i.e. a resort facility catering to high end clients.
I'm attaching the the website information, the flyer I created, logo files and pictures.

dev.brindlechildrenscenter.com Added Sunday, September 24, 2017

Target Market(s)

Parents of young children

Font styles to use
Other font styles liked:
• "Things we said" & "Calibri Light"

Colors
cfeae6
fef1ee

Requirements
Must have
• Pictures of children. sleek design - winter, mountain theme. Check with website designer on new website.
Nice to have
• prices included
Should not have
• Kid like artwork

```html
<!DOCTYPE html>
<html lang="en">
<head>
<meta charset="utf-8">
<title>Brindle Children's Center – Brochure</title>
<link href="https://fonts.googleapis.com/css2?family=Open+Sans:wght@400;600&family=Amatic+SC:wght@700&display=swap" rel="stylesheet">
<style>
  :root{
    --stage:#b3b3b3;
    --paper:#ffffff;
    --mint:#cfeae6;
    --mint-deep:#6fb7ad;
    --teal-dark:#2f6f67;
    --blush:#fef1ee;
    --orange:#e8623f;
    --ink:#333333;
    --rule:#9a9a9a;
  }
  *{box-sizing:border-box;margin:0;padding:0}
  html,body{width:1200px;height:1200px;overflow:hidden;background:var(--stage);font-family:"Open Sans",Arial,sans-serif;color:var(--ink)}
  .brochure{position:absolute;left:60px;top:216px;width:1080px;height:768px;display:flex;box-shadow:0 14px 30px rgba(0,0,0,.35);background:var(--paper)}
  .panel{position:relative;width:360px;height:768px;overflow:hidden}
  .panel--info{background:linear-gradient(180deg,#eef0f2 0%,#fafafa 25%,#ffffff 60%)}
  .panel--contact{background:linear-gradient(180deg,var(--mint) 0%,#e6f5f2 60%,#f4fbfa 100%)}
  .panel--cover{background:linear-gradient(180deg,#ffffff 0%,#f7f7f7 100%);box-shadow:inset 8px 0 14px -8px rgba(0,0,0,.18)}

  /* info panel */
  .info{position:absolute;left:26px;right:18px}
  .heading{color:var(--orange);font-size:16px;font-weight:400;letter-spacing:.2px}
  .heading .accent{color:var(--teal-dark)}
  .copy{font-size:10.5px;line-height:1.45;margin-top:4px;text-align:justify}
  .form-box{position:absolute;left:14px;right:14px;top:100px;height:150px;background:#fff;border-radius:14px;box-shadow:0 0 10px rgba(0,0,0,.08);padding:14px 16px}
  .form-line{display:flex;align-items:flex-end;font-size:10px;margin-top:9px}
  .form-line span{white-space:nowrap;margin-right:4px}
  .form-line i{flex:1;border-bottom:1px solid var(--rule);height:1px;margin-bottom:3px}
  .rates{position:absolute;left:26px;top:420px;width:320px}
  .rate-row{display:flex;font-size:10px;margin-top:6px}
  .rate-label{width:155px;color:var(--orange)}
  .rate-list{line-height:1.5}
  .rate-list b{color:var(--orange);font-weight:600}
  .photo{position:absolute}
  .photo--reading{left:0;bottom:0;width:360px;height:225px;background:radial-gradient(ellipse at 45% 55%,#c9a77c 0%,#d9c3a3 40%,#f3ece4 75%,rgba(255,255,255,0) 100%)}

  /* contact panel */
  .photo--forest{left:0;top:0;width:360px;height:300px;background:linear-gradient(180deg,#a9d6cf 0%,#5f9e95 45%,#9fd0c8 75%,rgba(207,234,230,0) 100%)}
  .circle{position:absolute;border-radius:50%;border:4px solid #fff;box-shadow:0 2px 6px rgba(0,0,0,.2)}
  .circle--play{left:52px;top:276px;width:142px;height:142px;background:radial-gradient(circle at 45% 50%,#f0d3b6,#c98f56 60%,#8a5a33)}
  .circle--art{left:190px;top:268px;width:146px;height:146px;background:radial-gradient(circle at 50% 45%,#f4c7b0,#d46d82 55%,#7a4d6b)}
  .logo{position:absolute;left:0;right:0;text-align:center;display:flex;flex-direction:column;align-items:center;gap:6px}
  .logo-mark{width:22px;height:22px;border-radius:50%;background:var(--ink)}
  .logo-name{font-size:13px;font-weight:600;color:var(--ink);letter-spacing:.5px;text-transform:uppercase}
  .contacts{position:absolute;left:0;right:0;top:590px;text-align:center;font-size:12px;line-height:23px}
  .contacts svg{width:11px;height:11px;vertical-align:-1px;margin-right:5px;fill:var(--ink)}
  .hours{position:absolute;left:80px;top:704px;width:200px;height:26px;border-radius:13px;background:var(--orange);color:#fff;font-size:14px;font-weight:600;text-align:center;line-height:26px}

  /* cover panel */
  .photo--lodge{left:0;top:0;width:360px;height:320px;background:linear-gradient(180deg,#c7d3de 0%,#9a7a5c 30%,#c2a384 55%,#e9eaec 80%,rgba(255,255,255,0) 100%)}
  .circle--craft{left:36px;top:232px;width:152px;height:152px;background:radial-gradient(circle at 50% 45%,#f2cdb5,#d0789a 55%,#6a5a74)}
  .circle--toys{left:186px;top:270px;width:142px;height:142px;background:radial-gradient(circle at 50% 45%,#e9eef2,#b9c7c9 55%,#8c7f6a)}
  .tagline{position:absolute;left:0;right:0;text-align:center;font-family:"Amatic SC",cursive;font-weight:700;line-height:1}
  .tagline--main{top:580px;font-size:38px;color:var(--ink)}
  .tagline--ages{top:622px;font-size:40px;color:var(--mint-deep)}
  .location{position:absolute;left:0;right:0;top:690px;text-align:center;color:var(--orange);font-size:14px;line-height:21px}
</style>
</head>
<body>
<main class="brochure">

  <section class="panel panel--info">
    <div class="info" style="top:22px">
      <h2 class="heading">RESERVATIONS</h2>
      <p class="copy">We highly recommend that reservations be made in advance to ensure space for your child. To make a reservation contact us at: 555-014-2290. We have limited capacity.</p>
    </div>
    <div class="form-box">
      <h2 class="heading">RESERVATION <span class="accent">CONFORMATION:</span></h2>
      <div class="form-line"><span>Conformation Number:</span><i></i></div>
      <div class="form-line"><span>Child's Name:</span><i></i></div>
      <div class="form-line"><span>Child's Age:</span><i></i></div>
      <div class="form-line"><span>Reserved Dates:</span><i></i></div>
      <div class="form-line"><span>Reservation Fee:</span><i></i></div>
    </div>
    <div class="info" style="top:264px">
      <p class="copy">Your reservation fee will be applied to your last day of service.</p>
    </div>
    <div class="info" style="top:300px">
      <h2 class="heading">CANCELLATION <span class="accent">POLICY</span></h2>
      <p class="copy">Reservations must be cancelled 24hrs in advance of the date(s) of service or full fee will be charged for all days not cancelled</p>
    </div>
    <div class="info" style="top:390px">
      <h2 class="heading" style="color:var(--teal-dark)">RATES</h2>
    </div>
    <div class="rates">
      <div class="rate-row">
        <span class="rate-label">Infant/Toddler/..................</span>
        <span class="rate-list"><b>$105</b>/full day<br><b>$90</b>/half day<br><b>$475</b>/Five day package</span>
      </div>
      <div class="rate-row" style="margin-top:10px">
        <span class="rate-label">3 years and Up:..................</span>
        <span class="rate-list"><b>$99</b>/full day<br><b>$85</b>/half day<br><b>$450</b>/Five day package</span>
      </div>
    </div>
    <div class="photo photo--reading" role="img" aria-label="Photo of a parent reading a picture book with a baby beside a large teddy bear"></div>
  </section>

  <section class="panel panel--contact">
    <div class="photo photo--forest" role="img" aria-label="Mint-tinted photo of snowy pine trees on a mountain slope"></div>
    <div class="circle circle--play" role="img" aria-label="Photo of a toddler playing with toys"></div>
    <div class="circle circle--art" role="img" aria-label="Photo of a girl drawing with a crayon"></div>
    <div class="logo" style="top:470px">
      <span class="logo-mark"></span>
      <span class="logo-name">Brindle Children's Center</span>
    </div>
    <div class="contacts">
      <div><svg viewBox="0 0 24 24"><path d="M6.6 10.8a15 15 0 0 0 6.6 6.6l2.2-2.2c.3-.3.7-.4 1-.2 1.1.4 2.3.6 3.6.6.6 0 1 .4 1 1V20c0 .6-.4 1-1 1A17 17 0 0 1 3 4c0-.6.4-1 1-1h3.5c.6 0 1 .4 1 1 0 1.3.2 2.5.6 3.6.1.3 0 .7-.2 1z"/></svg>(555) 014-2290</div>
      <div><svg viewBox="0 0 24 24"><circle cx="12" cy="12" r="10"/><path d="M6 9h12v7H6z" fill="#fff"/><path d="M6 9l6 4 6-4" stroke="#333" fill="none" stroke-width="1.4"/></svg>info@brindlechildrenscenter.com</div>
      <div><svg viewBox="0 0 24 24"><circle cx="12" cy="12" r="10"/><path d="M2 12h20M12 2c3 3 3 17 0 20M12 2c-3 3-3 17 0 20" stroke="#fff" fill="none" stroke-width="1.4"/></svg>www.brindlechildrenscenter.com</div>
      <div>P.O. Box 4410 Brindle, Utah 84000</div>
    </div>
    <div class="hours">Open daily: 8:30-4:30</div>
  </section>

  <section class="panel panel--cover">
    <div class="photo photo--lodge" role="img" aria-label="Photo of the ski lodge building with skiers on the snow in front"></div>
    <div class="circle circle--craft" role="img" aria-label="Photo of two young girls doing crafts at a table"></div>
    <div class="circle circle--toys" role="img" aria-label="Photo of children playing in a classroom"></div>
    <div class="logo" style="top:458px">
      <span class="logo-mark"></span>
      <span class="logo-name">Brindle Children's Center</span>
    </div>
    <p class="tagline tagline--main">SERVING CHILDREN AGES</p>
    <p class="tagline tagline--ages">6 WKS THRU 9 YEARS</p>
    <p class="location">(Located at the Summit Ticket<br>Office Building)</p>
  </section>

</main>
</body>
</html>
```